seeking a modern Business Card design for Roof Plumbering Business

wexcombe roof plumbing is a local metal re-roof and new construction specialist. We are seeking a modern business card to assist with networking within the industry. Our services are predominantly the installation of metal roofs on new houses, however we also do re-roofs when an existing roof needs replacing. We service both residential and commercial properties. Please include the below details on the card:
Name: Owen Wexcombe
Phone: 0471 385 962
Email: owenwexcomberoofing@mailnest.example

Residential & Commercial
Re-roof & New Construction
Fully Insured

I have uploaded our business logo, which we think would suit a black background. Please use all lower case for business name.
Cheers
Updates

Hey Guys, As requested I've uploaded a Pdf version of my logo. Hopefully this help. Thanks

Industry/Entity Type

Business

Contact Information for Business Card

Name: Owen Wexcombe
Phone: 0471 385 962

Residential & Commercial
Fully Insured

Font styles to use
Serif
Sans Serif

Requirements
Must have
• Name must be all lower case "wexcombe roof plumbing"
Nice to have
• Stick with Logo Colours

```html
<!DOCTYPE html>
<html lang="en">
<head>
<meta charset="UTF-8">
<title>wexcombe roof plumbing – business card</title>
<link rel="stylesheet" href="https://fonts.googleapis.com/css2?family=Arimo:wght@400;700&display=swap">
<style>
  :root {
    --page-bg: #e6e8ea;
    --card-white: #ffffff;
    --card-fade: #eeeeee;
    --brand-blue: #1fa4d8;
    --roof-grey: #8c8c8c;
    --text-grey: #555a5e;
    --divider-grey: #c9c9c9;
  }
  * { margin: 0; padding: 0; box-sizing: border-box; }
  html, body { width: 1200px; height: 950px; overflow: hidden; }
  body {
    background: var(--page-bg);
    font-family: "Arimo", Arial, sans-serif;
    position: relative;
  }
  .business-card {
    position: absolute;
    left: 100px;
    top: 190px;
    width: 1000px;
    height: 570px;
    background: linear-gradient(180deg, var(--card-white) 55%, var(--card-fade) 100%);
    border-radius: 6px;
    box-shadow: 0 12px 30px rgba(0,0,0,0.18);
    overflow: hidden;
  }
  .roof-band { position: absolute; inset: 0; width: 1000px; height: 570px; }
  .card-holder {
    position: absolute;
    right: 62px;
    top: 168px;
    text-align: right;
    color: var(--card-white);
  }
  .holder-name { font-size: 31px; font-weight: 700; letter-spacing: 0.3px; }
  .holder-title { font-size: 21px; margin-top: 8px; }
  .brand-name {
    position: absolute;
    left: 52px;
    top: 340px;
    width: 330px;
    display: flex;
    align-items: center;
    gap: 12px;
    color: var(--brand-blue);
    font-size: 27px;
    font-weight: 400;
    line-height: 1;
    white-space: nowrap;
  }
  .brand-square {
    width: 14px;
    height: 14px;
    background: var(--brand-blue);
    flex: none;
  }
  .divider {
    position: absolute;
    left: 400px;
    top: 270px;
    width: 2px;
    height: 190px;
    background: var(--divider-grey);
  }
  .contact-list {
    position: absolute;
    left: 432px;
    top: 290px;
    list-style: none;
    color: var(--text-grey);
    font-size: 23px;
  }
  .contact-list li { display: flex; align-items: center; height: 37px; }
  .contact-list svg { width: 20px; height: 20px; margin-right: 14px; flex: none; }
  .icon-fill { fill: var(--brand-blue); }
  .icon-stroke { fill: none; stroke: var(--brand-blue); stroke-width: 2.6; stroke-linecap: round; stroke-linejoin: round; }
</style>
</head>
<body>
  <article class="business-card">
    <svg class="roof-band" viewBox="0 0 1000 570" aria-hidden="true">
      <defs>
        <linearGradient id="bandGradient" x1="0" y1="0" x2="1" y2="1">
          <stop offset="0" stop-color="#1796cd"/>
          <stop offset="0.6" stop-color="#29b3e4"/>
          <stop offset="1" stop-color="#1a9ed6"/>
        </linearGradient>
      </defs>
      <polygon points="0,0 1000,0 1000,300 290,68 0,86" fill="url(#bandGradient)"/>
      <polyline points="0,100 290,82 1000,316" fill="none" stroke="var(--roof-grey)" stroke-width="7"/>
    </svg>

    <header class="card-holder">
      <div class="holder-name">Owen Wexcombe</div>
      <div class="holder-title">CEO/Founder</div>
    </header>

    <div class="brand-name">
      <span class="brand-square"></span>
      <span>wexcombe roof plumbing</span>
    </div>

    <div class="divider"></div>

    <ul class="contact-list">
      <li>
        <svg viewBox="0 0 20 20" aria-hidden="true"><path class="icon-fill" d="M4 7c0-2 2-4 6-4s6 2 6 4v1h-3V6.5H7V8H4z M5 9h10l2 7H3z"/><circle cx="10" cy="12.5" r="2" fill="#fff"/></svg>
        0471 385 962
      </li>
      <li>
        <svg viewBox="0 0 20 20" aria-hidden="true"><rect class="icon-fill" x="1" y="4" width="18" height="12" rx="1"/><polyline points="1.5,4.5 10,11 18.5,4.5" fill="none" stroke="#fff" stroke-width="1.6"/></svg>
        owenwexcomberoofing@mailnest.example
      </li>
      <li>
        <svg viewBox="0 0 20 20" aria-hidden="true"><polyline class="icon-stroke" points="3,10.5 8,15.5 17,4.5"/></svg>
        Fully Insured
      </li>
      <li>
        <svg viewBox="0 0 20 20" aria-hidden="true"><polyline class="icon-stroke" points="3,10.5 8,15.5 17,4.5"/></svg>
        Residential &amp; Commercial
      </li>
      <li>
        <svg viewBox="0 0 20 20" aria-hidden="true"><polyline class="icon-stroke" points="3,10.5 8,15.5 17,4.5"/></svg>
        Re-roof &amp; New Construction
      </li>
    </ul>
  </article>
</body>
</html>
```